Business Card Design

My company is a Consulting & Training company (Halvorn Consulting and Training, LLC) specializing in Firearms Training, State of Florida Concealed Weapons Permit Course, and Tactical Equipment Consulting.

Industry/Entity Type

Business

Contact Information for Business Card

Tobin Halvorn
P.O. Box 412763
Aventura, FL 33197
(786)555-0148

```html
<!DOCTYPE html>
<html lang="en">
<head>
<meta charset="utf-8">
<title>Halvorn Consulting and Training – Business Card</title>
<link href="https://fonts.googleapis.com/css2?family=Roboto+Condensed:wght@400;700&display=swap" rel="stylesheet">
<style>
  :root {
    --ink: #0a0a0a;
    --paper: #f4f4f4;
    --stage: #e6e3de;
    --photo-range-top: #e4e1de;
    --photo-range-bottom: #b9b4ae;
    --photo-items-top: #f7f7f6;
    --photo-items-bottom: #d8d6d2;
  }
  html, body {
    margin: 0;
    padding: 0;
    width: 1200px;
    height: 902px;
    overflow: hidden;
    background: var(--stage);
    font-family: "Roboto Condensed", Arial, sans-serif;
  }
  .canvas { position: relative; width: 1200px; height: 902px; }
  .card {
    position: absolute;
    top: 300px;
    width: 530px;
    height: 303px;
    border-radius: 16px;
    overflow: hidden;
    box-shadow: 0 10px 28px rgba(0,0,0,.25);
  }
  /* Front */
  .card-front { left: 50px; background: var(--ink); }
  .front-title-band {
    position: absolute; left: 0; top: 0; width: 100%; height: 66px;
    display: flex; align-items: center; justify-content: center;
  }
  .front-title {
    color: #fff; font-weight: 700; font-size: 31px; letter-spacing: .2px; white-space: nowrap;
  }
  .front-photo-band {
    position: absolute; left: 0; top: 66px; width: 100%; height: 176px;
    background: linear-gradient(180deg, #ffffff, var(--paper));
  }
  .photo-frame {
    position: absolute; top: 12px; height: 148px;
    border: 3px solid var(--ink); box-sizing: border-box; padding: 4px; background: #fff;
  }
  .photo-frame.left { left: 26px; width: 238px; }
  .photo-frame.right { left: 284px; width: 220px; }
  .photo-fill { width: 100%; height: 100%; }
  .photo-fill.range {
    background: linear-gradient(180deg, var(--photo-range-top), var(--photo-range-bottom));
  }
  .photo-fill.handguns {
    background: linear-gradient(180deg, var(--photo-items-top), var(--photo-items-bottom));
  }
  .front-address {
    position: absolute; right: 26px; bottom: 20px;
    color: #fff; font-size: 15px; white-space: nowrap;
  }
  /* Back */
  .card-back { left: 620px; background: var(--ink); }
  .back-head {
    position: absolute; left: 0; top: 0; width: 100%; height: 106px;
    background: linear-gradient(180deg, #ffffff, var(--paper));
  }
  .back-title {
    position: absolute; left: 0; width: 100%; top: 18px; text-align: center;
    color: var(--ink); font-weight: 700; font-size: 31px; white-space: nowrap;
  }
  .back-name {
    position: absolute; left: 0; width: 100%; top: 64px; text-align: center;
    color: #222; font-size: 21px;
  }
  .back-rule { position: absolute; left: 0; top: 106px; width: 100%; height: 10px; }
  .back-body {
    position: absolute; left: 0; top: 128px; width: 100%;
    text-align: center; color: #fff; font-size: 15px; line-height: 20px;
  }
  .service-heading { font-weight: 700; font-size: 17px; margin-top: 10px; }
</style>
</head>
<body>
<div class="canvas">

  <section class="card card-front">
    <div class="front-title-band">
      <div class="front-title">Halvorn Consulting and Training, LLC</div>
    </div>
    <div class="front-photo-band">
      <div class="photo-frame left">
        <div class="photo-fill range" role="img" aria-label="Photo of a pistol resting on a shooting target"></div>
      </div>
      <div class="photo-frame right">
        <div class="photo-fill handguns" role="img" aria-label="Photo of a pistol and a revolver with cartridges"></div>
      </div>
    </div>
    <div class="front-address">P.O. Box 412763 Aventura, FL 33197</div>
  </section>

  <section class="card card-back">
    <div class="back-head">
      <div class="back-title">Halvorn Consulting and Training, LLC</div>
      <div class="back-name">Tobin Halvorn</div>
    </div>
    <svg class="back-rule" viewBox="0 0 530 10" preserveAspectRatio="none">
      <rect x="0" y="0" width="530" height="4" fill="#0a0a0a"/>
      <rect x="0" y="4" width="530" height="3" fill="#f4f4f4"/>
      <rect x="0" y="7" width="530" height="3" fill="#0a0a0a"/>
    </svg>
    <div class="back-body">
      <div class="contact-phone">(786)555-0148</div>
      <div class="contact-email">HalvornCT@mailnest.com</div>
      <div class="contact-address">P.O. Box 412763 Aventura, FL 33197</div>
      <div class="service-heading">Service</div>
      <div class="service-item">Firearms Training</div>
      <div class="service-item">Tactical Equipment Consulting</div>
      <div class="service-item">State of Florida Concealed Weapons Permit Course</div>
    </div>
  </section>

</div>
</body>
</html>
```